Stationery Design Project

Please see all instructions for business card design. The stationary needs the same information.

I will need #10 envelopes, large letter size mailing envelopes, letterhead, return envelopes.

Industry/Entity Type

Business

```html
<!DOCTYPE html>
<html lang="en">
<head>
<meta charset="utf-8">
<title>Marlow Grant Financial – Stationery Set</title>
<link href="https://fonts.googleapis.com/css2?family=Cinzel:wght@500&family=Arimo:wght@400;700&display=swap" rel="stylesheet">
<style>
  :root{
    --board:#6d6d6d;
    --paper:#ffffff;
    --edge:#4a4a4a;
    --gold:#c9a13f;
    --red:#b51d1c;
    --wine:#7d1517;
    --ink:#1e1e1e;
    --mark:#2a1a12;
    --label:#f2f2f2;
    --footer-ink:#f3e0c0;
  }
  *{box-sizing:border-box;margin:0;padding:0}
  html,body{width:1200px;height:609px;overflow:hidden;background:var(--board)}
  .board{position:relative;width:1200px;height:609px;font-family:"Arimo",Arial,sans-serif}
  .sheet{position:absolute;background:var(--paper);overflow:hidden}
  .flap{position:absolute;inset:0;width:100%;height:100%}
  .flap path{fill:none;stroke:var(--edge);stroke-width:.8;vector-effect:non-scaling-stroke}
  .brand{position:absolute;display:flex;flex-direction:column;align-items:center;gap:2px}
  .brand.left{align-items:flex-start}
  .brand.left .brand-mark{margin-left:18px}
  .brand-mark{width:9px;height:9px;background:var(--mark);flex:none}
  .brand-name{font-family:"Cinzel",Georgia,serif;font-weight:500;color:var(--gold);font-size:5.4px;letter-spacing:.1px;white-space:nowrap;line-height:7px}
  .brand.side{left:268px;top:0;width:32px;height:100%;flex-direction:row;justify-content:center;align-items:center;writing-mode:vertical-rl;gap:3px}
  .address{position:absolute;font-size:4.4px;line-height:5.4px;color:var(--ink);white-space:nowrap}
  .band{position:absolute;left:0;bottom:0;width:100%;background:linear-gradient(180deg,var(--gold) 0%,var(--red) 48%,var(--wine) 100%)}
  .label{position:absolute;text-align:center;color:var(--label);font-weight:700;font-size:9px;line-height:11.5px}
  .label.light{font-weight:400}
  .from{position:absolute;left:12px;top:10px;font-size:3.8px;color:var(--ink)}
  .from-lines{position:absolute;left:28px;top:9px;width:60px}
  .from-lines span{display:block;border-bottom:.6px solid var(--edge);height:5px}
  .stamp{position:absolute;right:8px;top:8px;width:20px;height:22px;border:.6px solid var(--edge);display:flex;align-items:center;justify-content:center;text-align:center;font-size:3px;line-height:3.6px;color:var(--ink)}
  .lh-rule{position:absolute;left:0;width:118px;top:36px;height:.6px;background:var(--gold)}
  .lh-tagline{position:absolute;left:12px;top:38px;font-size:2.9px;color:var(--gold);white-space:nowrap}
  .lh-contact{position:absolute;right:8px;top:13px;text-align:right;font-size:3.4px;line-height:3.9px;color:var(--ink);white-space:nowrap}
  .lh-contact .lh-address{display:block;margin-top:1.5px}
  .lh-footer{position:absolute;left:20px;right:20px;bottom:3px;text-align:center;font-size:2.7px;line-height:3.3px;color:var(--footer-ink)}
</style>
</head>
<body>
<main class="board">

  <!-- Large mailing envelope, side flap -->
  <section class="sheet" style="left:13px;top:79px;width:300px;height:211px">
    <svg class="flap" viewBox="0 0 300 211" preserveAspectRatio="none"><path d="M300 0 L268 22 L268 189 L300 211"/></svg>
    <div class="brand side"><span class="brand-name">Marlow Grant Financial</span><span class="brand-mark"></span></div>
  </section>
  <p class="label" style="left:13px;top:297px;width:300px">large letter size mailing envelope<br>324 mm x 229 mm</p>
  <section class="sheet" style="left:13px;top:331px;width:300px;height:211px">
    <div class="brand left" style="left:18px;top:18px"><span class="brand-mark"></span><span class="brand-name">Marlow Grant Financial</span></div>
    <p class="address" style="left:18px;top:38px">480 West Alder Street<br>Suite 210<br>Fairview, CA 95012</p>
    <div class="band" style="height:28px" role="img" aria-label="Decorative gold and wine sweeping band"></div>
  </section>

  <!-- Large mailing envelope, top flap -->
  <section class="sheet" style="left:350px;top:79px;width:300px;height:211px">
    <svg class="flap" viewBox="0 0 300 211" preserveAspectRatio="none"><path d="M0 0 L24 36 L276 36 L300 0"/></svg>
    <div class="brand" style="left:0;right:0;top:12px"><span class="brand-mark"></span><span class="brand-name">Marlow Grant Financial</span></div>
  </section>
  <p class="label light" style="left:350px;top:297px;width:300px">large letter size mailing envelope<br>229 mm x 324 mm</p>
  <section class="sheet" style="left:350px;top:331px;width:300px;height:211px">
    <div class="brand left" style="left:18px;top:18px"><span class="brand-mark"></span><span class="brand-name">Marlow Grant Financial</span></div>
    <p class="address" style="left:18px;top:38px">480 West Alder Street<br>Suite 210<br>Fairview, CA 95012</p>
    <div class="band" style="height:28px" role="img" aria-label="Decorative gold and wine sweeping band"></div>
  </section>

  <!-- Letter size small mailing envelope -->
  <section class="sheet" style="left:673px;top:18px;width:270px;height:142px">
    <svg class="flap" viewBox="0 0 270 142" preserveAspectRatio="none"><path d="M0 0 L22 36 L248 36 L270 0"/></svg>
    <div class="brand" style="left:0;right:0;top:14px"><span class="brand-mark"></span><span class="brand-name">Marlow Grant Financial</span></div>
  </section>
  <p class="label" style="left:673px;top:172px;width:270px">letter size small mailing envelope<br>155,575 mm&nbsp; x 292,1 mm</p>
  <section class="sheet" style="left:673px;top:201px;width:270px;height:143px">
    <div class="brand left" style="left:18px;top:18px"><span class="brand-mark"></span><span class="brand-name">Marlow Grant Financial</span></div>
    <p class="address" style="left:18px;top:37px">480 West Alder Street<br>Suite 210<br>Fairview, CA 95012</p>
    <div class="band" style="height:26px" role="img" aria-label="Decorative gold and wine sweeping band"></div>
  </section>

  <!-- #10 envelope -->
  <section class="sheet" style="left:698px;top:366px;width:223px;height:96px">
    <svg class="flap" viewBox="0 0 223 96" preserveAspectRatio="none"><path d="M0 0 L20 32 L203 32 L223 0"/></svg>
    <div class="brand" style="left:0;right:0;top:11px"><span class="brand-mark"></span><span class="brand-name">Marlow Grant Financial</span></div>
  </section>
  <p class="label" style="left:698px;top:468px;width:223px">#10 envelope<br>104,775 mm x 241,3 mm</p>
  <section class="sheet" style="left:698px;top:496px;width:223px;height:96px">
    <div class="brand left" style="left:14px;top:12px"><span class="brand-mark"></span><span class="brand-name">Marlow Grant Financial</span></div>
    <p class="address" style="left:14px;top:31px">480 West Alder Street<br>Suite 210<br>Fairview, CA 95012</p>
    <div class="band" style="height:22px" role="img" aria-label="Decorative gold and wine sweeping band"></div>
  </section>

  <!-- Return envelope -->
  <section class="sheet" style="left:964px;top:18px;width:223px;height:96px">
    <svg class="flap" viewBox="0 0 223 96" preserveAspectRatio="none"><path d="M0 0 L20 31 L203 31 L223 0"/></svg>
    <div class="brand" style="left:0;right:0;top:9px"><span class="brand-mark"></span><span class="brand-name">Marlow Grant Financial</span></div>
  </section>
  <p class="label" style="left:964px;top:126px;width:223px">return envelopes<br>104,775 mm x 241,3 mm</p>
  <section class="sheet" style="left:964px;top:158px;width:223px;height:96px">
    <span class="from">FROM</span>
    <div class="from-lines"><span></span><span></span><span></span></div>
    <div class="stamp">PLACE<br>STAMP<br>HERE</div>
    <div class="brand left" style="left:10px;top:48px"><span class="brand-mark"></span><span class="brand-name">Marlow Grant Financial</span></div>
    <p class="address" style="left:92px;top:52px">480 West Alder Street<br>Suite 210<br>Fairview, CA 95012</p>
    <div class="band" style="height:22px" role="img" aria-label="Decorative gold and wine sweeping band"></div>
  </section>

  <!-- Letterhead -->
  <section class="sheet" style="left:975px;top:312px;width:200px;height:258px">
    <div class="brand left" style="left:12px;top:16px"><span class="brand-mark"></span><span class="brand-name">Marlow Grant Financial</span></div>
    <div class="lh-rule"></div>
    <p class="lh-tagline">Planning for lasting independence</p>
    <p class="lh-contact">Phone: 555-014-2200<br>Fax: 555-014-2213<br>Email: info@marlowgrantfinancial.com<br>www.marlowgrantfinancial.com<span class="lh-address">480 West Alder Street, Suite 210<br>Fairview, CA 95012</span></p>
    <div class="band" style="height:26px" role="img" aria-label="Decorative gold and wine sweeping band"></div>
    <p class="lh-footer">Marlow Grant Financial offers securities through an independent registered broker-dealer and adviser.</p>
  </section>
  <p class="label" style="left:975px;top:575px;width:200px">letterhead</p>
</main>
</body>
</html>
```